Website Needs a New Look & Feel - I am Too Old and Uncool on my Own

I want some design ideas for my current site. I need a new, more modern and dynamic look and feel. The audience for the site is 90% male, 24-54 years old, and not highly educated. English is second language for about 30% of audience, so images help. 85% of visitors view on mobile. We sell trucks and trailers to this audience. . Just want something new and cool. Tired of what I have. Current site doesn't seem strong enough to match the kind of people who drive trucks for a living. Current is site is brelvon.com. Pull relevant menu and text from the site.

Target Market(s)

Truck Drivers and Trucking Company Owners (90% male).

Industry/Entity Type

Transportation - Specifically, truck and trailer sales.

Number of Pages Required

3 page

Font styles to use
Sans Serif

Colors
0054AA
0677BA
7BADD7
CADEEF
E8F1F8

Requirements
Must have
• Images of Sleeper Trucks (like on there now) and trailers. Audience is very literal, so they need to see what we sell.
Nice to have
• Images of Sleeper Trucks (like on tMy inventory pages are boring, please show me something more user-friendly and interesting. here now) and trailers.

```html
<!DOCTYPE html>
<html lang="en">
<head>
<meta charset="utf-8">
<title>Brelvon Truck &amp; Trailer</title>
<link href="https://fonts.googleapis.com/css2?family=Outfit:wght@300;400;500;600;700&display=swap" rel="stylesheet">
<style>
:root{
  --navy:#1a2c55;
  --navy-deep:#14223f;
  --blue:#1f4c9c;
  --blue-bright:#2559b0;
  --page:#f2f3fa;
  --band:#e4e6ec;
  --ink:#1b1f2a;
  --white:#ffffff;
  --star:#f2a31b;
  --sky:#c9d6e6;
  --truck-blue:#1d4594;
  --truck-red:#c9262f;
  --chrome:#dfe2e7;
  --asphalt:#3b3e45;
}
*{box-sizing:border-box;margin:0;padding:0}
html,body{width:1200px;height:3630px;overflow:hidden}
body{font-family:'Outfit',sans-serif;background:var(--page);color:var(--ink);position:relative}
.abs{position:absolute}
.center{text-align:center}

/* header + hero */
.hero-photo{left:0;top:0;width:1200px;height:745px;
  background:
   radial-gradient(ellipse 70px 55px at 590px 490px,rgba(201,38,47,.85),rgba(201,38,47,0) 100%),
   radial-gradient(ellipse 90px 60px at 330px 500px,rgba(232,235,240,.8),rgba(232,235,240,0) 100%),
   radial-gradient(ellipse 80px 55px at 730px 505px,rgba(232,235,240,.75),rgba(232,235,240,0) 100%),
   radial-gradient(ellipse 110px 70px at 120px 500px,rgba(29,69,148,.9),rgba(29,69,148,0) 100%),
   radial-gradient(ellipse 120px 70px at 940px 500px,rgba(29,69,148,.9),rgba(29,69,148,0) 100%),
   linear-gradient(180deg,#e3e8f0 0%,#d0d8e3 20%,#b4bcc8 34%,#8d97a6 44%,#2a4f98 52%,#1e438d 62%,#5b6170 70%,#44474e 80%,#34363c 100%)}
.hero-curve{left:0;top:0}
.logo{left:93px;top:24px;color:var(--ink);font-weight:600;line-height:1}
.logo .l1{font-size:30px;letter-spacing:1px}
.logo .l2{font-size:16px;margin-top:3px}
.nav{left:340px;top:43px;display:flex;gap:22px;font-size:13.5px;font-weight:500;color:var(--ink);align-items:center}
.nav svg{display:block}
.btn{display:flex;align-items:center;justify-content:center;gap:8px;color:var(--white);font-weight:500;border-radius:3px;background:var(--blue)}
.dot-icon{width:16px;height:16px;border-radius:50%;border:2px solid var(--white);flex:none}
.nav-cta{left:903px;top:27px;width:202px;height:46px;font-size:14px}
.hero-title{left:0;width:1200px;top:152px;font-size:46px;font-weight:600;line-height:54px;color:var(--ink)}
.hero-btn{top:292px;height:41px;font-size:14px;font-weight:500;color:var(--white);display:flex;align-items:center;justify-content:center}
.hero-btn.dark{left:420px;width:188px;background:var(--navy-deep);clip-path:polygon(0 0,100% 0,96% 100%,0 100%)}
.hero-btn.blue{left:597px;width:184px;background:var(--blue);clip-path:polygon(5% 0,100% 0,100% 100%,0 100%)}
.hero-hub{left:571px;top:619px;width:60px;height:60px;border-radius:50%;background:#e7e9ee;border:12px solid var(--navy-deep)}

h2.section-title{position:absolute;left:0;width:1200px;text-align:center;font-size:37px;font-weight:600;color:var(--ink)}

/* inventory */
.inv-card{top:793px;width:249px;height:231px;background:#eef0f8;border:1px solid #d7dbe8;box-shadow:0 3px 6px rgba(20,30,60,.08);overflow:hidden}
.inv-card::before{content:"";position:absolute;right:-40px;top:-30px;width:200px;height:190px;background:#e3e7f5;transform:rotate(-28deg)}
.inv-card .photo{position:absolute;left:20px;top:22px;width:209px;height:140px}
.inv-card .label{position:absolute;left:0;right:0;top:188px;text-align:center;font-size:15px;font-weight:600}

/* wholesale */
.wh-ring{left:124px;top:1130px;width:420px;height:420px;border-radius:50%;border:6px solid var(--navy)}
.wh-photo{left:118px;top:1130px;width:416px;height:416px;border-radius:50%;
  background:
   radial-gradient(ellipse 150px 130px at 140px 200px,rgba(240,242,245,.95),rgba(240,242,245,0) 100%),
   radial-gradient(ellipse 110px 140px at 310px 150px,rgba(122,154,78,.85),rgba(122,154,78,0) 100%),
   linear-gradient(180deg,#cfe0f2 0%,#a9c3e0 35%,#e2e5ea 60%,#cfd2d6 78%,#8c8f88 100%)}
.wh-title{left:624px;top:1160px;font-size:32px;font-weight:600;line-height:45px;width:460px}
.wh-text{left:624px;top:1262px;width:420px;font-size:16px;line-height:26px;color:#3a4050;font-weight:300}
.wh-btn{left:624px;top:1466px;width:148px;height:41px;font-size:14px;background:var(--blue)}
.side-bar{left:1185px;top:1095px;width:15px;height:450px;background:var(--blue)}

/* finance / sell */
.split{left:93px;top:1649px;width:1012px;height:311px;overflow:hidden}
.split .fin{position:absolute;inset:0;background:radial-gradient(ellipse 160px 200px at 400px 200px,#5a5448,rgba(58,62,74,0)),linear-gradient(120deg,#2b3345,#3a4052 50%,#252b38)}
.split .sell{position:absolute;inset:0;background:linear-gradient(180deg,#2c5aa6,#1d4390);clip-path:polygon(532px 0,100% 0,100% 100%,480px 100%)}
.split .gap{position:absolute;inset:0;background:var(--white);clip-path:polygon(522px 0,532px 0,480px 100%,470px 100%)}
.panel-txt{position:absolute;color:var(--white);text-align:center}
.panel-txt h3{font-size:27px;font-weight:600}
.panel-txt p{font-size:13px;line-height:19px;font-weight:300}
.panel-txt .sub{font-size:18px;font-weight:400;margin-top:10px;line-height:22px}
.split-hub{left:559px;top:1762px;width:86px;height:86px;border-radius:50%;background:var(--white);display:flex;align-items:center;justify-content:center}
.split-hub span{width:66px;height:66px;border-radius:50%;background:#dfe2e8;border:14px solid #1c1d22}
.panel-btn{position:absolute;height:36px;font-size:13px;background:var(--blue-bright);border-radius:3px}

/* arrivals */
.arrivals{left:0;top:2056px;width:1200px;height:553px;background:var(--band)}
.car-card{top:2180px;width:247px;height:323px;background:var(--white)}
.car-card.active{border-bottom:3px solid var(--blue)}
.car-card .photo{position:absolute;left:7px;top:7px;width:233px;height:186px}
.car-card .name{position:absolute;left:0;right:0;top:210px;text-align:center;font-size:13px;line-height:17px;font-weight:400}
.car-card .price{position:absolute;left:0;right:0;top:247px;text-align:center;font-size:16px;font-weight:600;color:var(--blue)}
.car-card .view{position:absolute;left:70px;top:273px;width:107px;height:28px;font-size:11px;background:var(--blue);border-radius:3px}
.dots{left:579px;top:2531px;display:flex;gap:6px}
.dots span{width:9px;height:9px;border-radius:50%;background:#c6c9d2}
.dots span.on{background:var(--blue)}

/* testimonials */
.faint{border-radius:50%;background:#e3e5ee;border:16px solid #e9ebf2}
.quote{top:2753px;height:186px;background:var(--white);clip-path:polygon(4% 0,100% 0,96% 100%,0 100%)}
.quote p{position:absolute;left:36px;top:36px;width:260px;font-size:12.5px;line-height:20px;font-style:italic;font-weight:300;color:#444a5a}
.quote .who{position:absolute;left:110px;top:152px;font-size:13px;font-weight:600;display:flex;align-items:center;gap:10px}
.quote .stars{color:var(--star);font-size:11px;border-left:1px solid #ddd;padding-left:10px;letter-spacing:1px}
.avatar{width:54px;height:54px;border-radius:50%;background:linear-gradient(160deg,#d9dde5,#9aa2b2);border:4px solid var(--white);box-shadow:0 2px 5px rgba(0,0,0,.15)}
.arrow{width:34px;height:34px;border-radius:50%;display:flex;align-items:center;justify-content:center}

/* skyline + footer */
.skyline{left:0;top:3030px;width:1200px;height:217px;background:linear-gradient(180deg,rgba(26,44,85,0) 0%,rgba(26,44,85,.2) 35%,rgba(26,44,85,.75) 75%,var(--navy) 100%)}
.footer{left:0;top:3245px;width:1200px;height:385px;background:var(--navy)}
.f-h{position:absolute;color:var(--white);font-size:19px;font-weight:500}
.f-t{position:absolute;color:#dfe4ef;font-size:14px;line-height:22px;font-weight:300}
.f-ic{position:absolute;width:36px;height:36px;border-radius:50%;background:#3b4a6e;display:flex;align-items:center;justify-content:center}
.f-links{position:absolute;left:501px;top:3333px;list-style:none;font-size:14px;color:#dfe4ef;font-weight:300}
.f-links li{height:27px;display:flex;align-items:center;gap:8px}
.f-in{position:absolute;left:676px;width:310px;border:1px solid #4d5b7e;background:var(--navy-deep);color:#aeb7cb;font-size:13.5px;padding:9px 18px;font-weight:300}
.soc{position:absolute;top:3467px;width:31px;height:31px;border-radius:50%;background:var(--blue-bright)}
.f-send{left:676px;top:3505px;width:122px;height:36px;font-size:14px;background:var(--blue-bright)}
.f-rule{left:190px;top:3569px;width:820px;height:1px;background:#34446a}
.copy{left:0;width:1200px;top:3586px;text-align:center;font-size:13px;color:#9aa5be;font-weight:300}
</style>
</head>
<body>

<!-- hero -->
<div class="abs hero-photo" role="img" aria-label="Row of blue, white and red semi trucks parked in a yard under a cloudy sky"></div>
<svg class="abs hero-curve" width="1200" height="760" viewBox="0 0 1200 760">
  <path d="M0 745 Q600 565 1200 745 L1200 760 L0 760 Z" fill="#f2f3fa"/>
  <path d="M0 745 Q600 565 1200 745" fill="none" stroke="#14223f" stroke-width="3"/>
</svg>
<div class="abs hero-hub"></div>

<div class="abs logo"><div class="l1">BRELVON</div><div class="l2">Truck &amp; Trailer</div></div>
<nav class="abs nav">
  <svg width="16" height="14" viewBox="0 0 16 14"><path d="M8 0 L16 7 H13.5 V14 H9.5 V9.5 H6.5 V14 H2.5 V7 H0 Z" fill="#1f4c9c"/></svg>
  <span>SLEEPERS</span><span>REEFERS</span><span>DRY VANS</span><span>CRANES</span>
  <span>RESOURCES <svg style="display:inline" width="9" height="6" viewBox="0 0 9 6"><path d="M1 1 L4.5 4.5 L8 1" fill="none" stroke="#1b1f2a" stroke-width="1.2"/></svg></span>
  <span>CONTACT</span>
</nav>
<div class="abs btn nav-cta"><span class="dot-icon"></span>EXPLORE INVENTORY</div>

<h1 class="abs hero-title center">Drive your business forward<br>with our premium trailers!</h1>
<div class="abs hero-btn dark">EXPLORE INVENTORY</div>
<div class="abs hero-btn blue">GET FINANCING</div>

<!-- inventory -->
<h2 class="section-title" style="top:722px">ALL INVENTORY</h2>
<div class="abs inv-card" style="left:93px"><div class="photo" role="img" aria-label="White refrigerated reefer trailer with cooling unit" style="background:radial-gradient(ellipse 95px 45px at 105px 70px,#f7f8fa 40%,#cfd3db 80%,rgba(207,211,219,0) 100%)"></div><div class="label">REEFER TRAILERS</div></div>
<div class="abs inv-card" style="left:348px"><div class="photo" role="img" aria-label="Silver sleeper truck" style="background:radial-gradient(ellipse 80px 60px at 105px 72px,#d6dae1 30%,#8e949f 75%,rgba(142,148,159,0) 100%)"></div><div class="label">SLEEPERS</div></div>
<div class="abs inv-card" style="left:603px"><div class="photo" role="img" aria-label="White dry van trailer" style="background:radial-gradient(ellipse 95px 48px at 105px 72px,#fbfbfc 40%,#c4c9d2 80%,rgba(196,201,210,0) 100%)"></div><div class="label">DRY VANS</div></div>
<div class="abs inv-card" style="left:858px"><div class="photo" role="img" aria-label="Rough terrain mobile crane with extended boom" style="background:radial-gradient(ellipse 95px 30px at 105px 75px,#a09a82 30%,#5d5e62 70%,rgba(93,94,98,0) 100%)"></div><div class="label">CRANES</div></div>

<!-- wholesale -->
<div class="abs wh-ring"></div>
<div class="abs wh-photo" role="img" aria-label="White sleeper truck parked beside a green tree"></div>
<h2 class="abs wh-title">WHOLESALE REEFERS, DRY VANS, &amp; SLEEPERS</h2>
<p class="abs wh-text">Brelvon Truck &amp; Trailer is an equipment dealership in Kansas City, offering wholesale reefers, dry vans, and sleepers at the best prices. We aren't a normal dealership, because you can buy directly from us at wholesale price and save thousands. We don't have a fancy sales lot, but we do have the lowest prices on good, clean equipment in the country.</p>
<div class="abs btn wh-btn"><span class="dot-icon"></span>LEARN MORE</div>
<div class="abs side-bar"></div>

<!-- financing / sell -->
<div class="abs split">
  <div class="fin" role="img" aria-label="Stacks of coins on a dark desk"></div>
  <div class="sell" role="img" aria-label="Trucks in a yard with blue overlay"></div>
  <div class="gap"></div>
  <div class="panel-txt" style="left:78px;top:50px;width:300px">
    <h3>FINANCING</h3>
    <p style="margin-top:6px">Need Financing?&nbsp; We can help! Complete our finance form with no effect on your credit!</p>
    <div class="sub">GET PRE QUALIFIED!</div>
    <p>Get your payment, down payment &amp; term<br>with effect on your credit</p>
  </div>
  <div class="btn panel-btn" style="left:166px;top:223px;width:133px"><span class="dot-icon"></span>LEARN MORE</div>
  <div class="panel-txt" style="left:584px;top:50px;width:370px">
    <h3>SELL YOUR EQUIPMENT</h3>
    <p style="margin-top:6px">Have More Equipment Than You Need?</p>
    <p style="margin-top:14px">You Can Spend An Hour Filling Out Forms On Other Websites, Or You Can Just Give Us A Call. We'll Be Glad To Talk To You About What You Have To Sell, And How We Will Help You Get The Highest Price.</p>
  </div>
  <div class="btn panel-btn" style="left:672px;top:224px;width:195px"><span class="dot-icon"></span>REQUEST A CALL BACK</div>
</div>
<div class="abs split-hub"><span></span></div>

<!-- latest arrivals -->
<div class="abs arrivals"></div>
<h2 class="section-title" style="top:2112px">LATEST ARRIVALS</h2>
<div class="abs car-card" style="left:93px"><div class="photo" role="img" aria-label="Silver sleeper truck parked in a lot" style="background:radial-gradient(ellipse 80px 70px at 120px 95px,#e4e7ec 35%,rgba(228,231,236,0) 100%),linear-gradient(180deg,#aab6c6 0%,#c3cad4 40%,#7d838d 75%,#55585e 100%)"></div><div class="name">2022 Haulmark Ridgeline<br>126 – 463,830 Miles</div><div class="price">$ 74,500</div><div class="btn view">VIEW DETAILS</div></div>
<div class="abs car-card active" style="left:349px"><div class="photo" role="img" aria-label="Dark grey sleeper truck" style="background:radial-gradient(ellipse 90px 75px at 130px 95px,#5e626b 40%,rgba(94,98,107,0) 100%),linear-gradient(180deg,#c7ccd3 0%,#9a9fa8 40%,#6d7078 75%,#8e9096 100%)"></div><div class="name">2022 Haulmark<br>Ridgeline 126 – 466,680 Miles</div><div class="price">$ 74,500</div><div class="btn view">VIEW DETAILS</div></div>
<div class="abs car-card" style="left:604px"><div class="photo" role="img" aria-label="White sleeper truck under blue sky" style="background:radial-gradient(ellipse 95px 65px at 110px 100px,#f3f4f6 40%,rgba(243,244,246,0) 100%),linear-gradient(180deg,#6f9bd4 0%,#a9c4e6 40%,#c9ccd0 70%,#8b8a7c 100%)"></div><div class="name">2020 HAULMARK<br>Ridgeline – 319,417 Miles</div><div class="price">$ 63,000</div><div class="btn view">VIEW DETAILS</div></div>
<div class="abs car-card" style="left:859px"><div class="photo" role="img" aria-label="White sleeper truck under blue sky" style="background:radial-gradient(ellipse 95px 65px at 110px 100px,#f3f4f6 40%,rgba(243,244,246,0) 100%),linear-gradient(180deg,#6f9bd4 0%,#a9c4e6 40%,#c9ccd0 70%,#8b8a7c 100%)"></div><div class="name">2020 HAULMARK<br>Ridgeline – 387,829 Miles</div><div class="price">$ 61,250</div><div class="btn view">VIEW DETAILS</div></div>
<div class="abs dots"><span class="on"></span><span></span><span></span></div>

<!-- testimonials -->
<h2 class="section-title" style="top:2686px">WHAT OUR CLIENTS SAY</h2>
<div class="abs faint" style="left:890px;top:2683px;width:134px;height:134px"></div>
<div class="abs faint" style="left:148px;top:2880px;width:132px;height:132px"></div>
<div class="abs quote" style="left:239px;width:345px"><p>Lorem Ipsum is simply dummy text of the printing and typesetting industry. Lorem Ipsum has been the industry's standard dummy text ever since the 1500s, when an unknown printer took</p><div class="who">DAREK <span class="stars">★★★★★</span></div></div>
<div class="abs quote" style="left:608px;width:349px"><p>Lorem Ipsum is simply dummy text of the printing and typesetting industry. Lorem Ipsum has been the industry's standard dummy text ever since the 1500s, when an unknown printer took</p><div class="who">DAREK <span class="stars">★★★★★</span></div></div>
<div class="abs avatar" style="left:281px;top:2925px" role="img" aria-label="Customer portrait"></div>
<div class="abs avatar" style="left:647px;top:2925px" role="img" aria-label="Customer portrait"></div>
<div class="abs arrow" style="left:173px;top:2830px;background:#d5d8e2"><svg width="16" height="12" viewBox="0 0 16 12"><path d="M15 6 H2 M6 1 L1 6 L6 11" fill="none" stroke="#fff" stroke-width="2"/></svg></div>
<div class="abs arrow" style="left:991px;top:2830px;background:var(--blue)"><svg width="16" height="12" viewBox="0 0 16 12"><path d="M1 6 H14 M10 1 L15 6 L10 11" fill="none" stroke="#fff" stroke-width="2"/></svg></div>

<!-- skyline + footer -->
<div class="abs skyline" role="img" aria-label="Silhouette of construction cranes, workers, buildings and a trailer"></div>
<footer class="abs footer"></footer>

<div class="f-h" style="left:189px;top:3292px">CONTACT US</div>
<div class="f-ic" style="left:192px;top:3333px"><svg width="12" height="17" viewBox="0 0 12 17"><rect x="1" y="1" width="10" height="15" rx="2" fill="none" stroke="#fff" stroke-width="1.5"/><circle cx="6" cy="13" r="1" fill="#fff"/></svg></div>
<div class="f-t" style="left:252px;top:3335px">913-555-0147<br>Support 24/7 Weekdays</div>
<div class="f-ic" style="left:192px;top:3396px"><svg width="16" height="12" viewBox="0 0 16 12"><rect x="1" y="1" width="14" height="10" rx="1" fill="none" stroke="#fff" stroke-width="1.5"/><path d="M1 1 L8 7 L15 1" fill="none" stroke="#fff" stroke-width="1.5"/></svg></div>
<div class="f-t" style="left:252px;top:3405px">info@brelvon.com</div>
<div class="soc" style="left:202px" role="img" aria-label="Social link"></div>
<div class="soc" style="left:240px" role="img" aria-label="Social link"></div>
<div class="soc" style="left:278px" role="img" aria-label="Social link"></div>
<div class="soc" style="left:317px" role="img" aria-label="Social link"></div>

<div class="f-h" style="left:501px;top:3292px">Info</div>
<ul class="f-links">
  <li>› Sleepers</li><li>› Reefers</li><li>› Dry Vans</li><li>› Cranes</li><li>› Resources</li><li>› Contact</li>
</ul>

<div class="f-h" style="left:673px;top:3292px">Get In Touch</div>
<div class="f-in" style="top:3341px;height:34px">Your Name</div>
<div class="f-in" style="top:3386px;height:34px">Your Email Address</div>
<div class="f-in" style="top:3429px;height:63px">Comments</div>
<div class="abs btn f-send">Send To Us</div>

<div class="abs f-rule"></div>
<div class="abs copy">© Copyright 2026 Brelvon</div>

</body>
</html>
```